Brochure Design Project

1.We need a brochure design for our event program and invitation.

2.We must be able to print out the brochure and also send it out via email to participants.

3.We want the whole design to relate to "Cross-Examination","International Arbitration" atmosphere.

4.We want the design to look a bit (but not too) fancy and be readable.

Reason: There are only 2 of 6 designs we like. But we still need more options to choose.

Target Market(s)

Our audiences are all Chinese and International Lawyers

Industry/Entity Type

Event

Requirements
Must have
• 1. The brochure needs to actually reflect “cross-examination” on the cover. The title should go at the top of the page.

2. The brochure needs to make room for organizers and supporters’ logo. This is a cooperation event.

3. It is important that the text is a big enough to be read easily. At the moment we have been using Helvetica font at size 9 or 10. Helvetica is easily readable at this size.

4. The brochure color needs to be in line with our logo color, such as Green-Blue and white. Please suggest a color that also fits the organizers’ logo.

5. We need a pdf version and print out version. They are all A4 size. The pdf version size must be under 2 MB. Otherwise it’s difficult to send out as well as receive. For the printing version, when designing you need to leave a 4mm bleed over the page size. This bleed is important - otherwise the picture will not necessarily go to the edge of the cut. You also need to make sure that the text is not too close to the boundary. I tend to leave a 4-5mm margin for text within this on all sides.

6. Use the same font style as suggested in the draft program and invitation.
Nice to have
• A picture which represents the idea of cross-examination. I will send you the example pic.
Should not have
• 1. Should not be aggressive;

2. Should not be too fancy or too conservative;

3. Should not be too colorful

```html
<!DOCTYPE html>
<html lang="en">
<head>
<meta charset="utf-8">
<title>General Course Description</title>
<link href="https://fonts.googleapis.com/css2?family=Roboto:wght@300;400&display=swap" rel="stylesheet">
<style>
  :root {
    --brand-blue: #0a6ab4;
    --heading-blue: #1b73bd;
    --accent-red: #8a1c1c;
    --body-grey: #585858;
    --lead-grey: #3a3a3a;
    --paper: #ffffff;
  }
  * { margin: 0; padding: 0; box-sizing: border-box; }
  html, body { width: 1200px; height: 851px; overflow: hidden; background: var(--paper); }
  body { font-family: "Roboto", Helvetica, Arial, sans-serif; font-weight: 300; color: var(--body-grey); }
  .spread { position: relative; width: 1200px; height: 851px; background: var(--paper); }

  .edge-tab { position: absolute; top: 142px; width: 40px; height: 98px; background: var(--brand-blue); }
  .edge-tab--left { left: 0; }
  .edge-tab--right { right: 0; }

  .column { position: absolute; font-size: 11.4px; line-height: 18.6px; }
  .column--left { left: 81px; top: 136px; width: 482px; }
  .column--right { left: 640px; top: 135px; width: 470px; }

  .page-title { font-size: 27px; font-weight: 300; color: var(--heading-blue); line-height: 34px; margin-bottom: 30px; }
  .section-title { font-size: 14.5px; font-weight: 400; color: var(--accent-red); margin-bottom: 9px; }
  .lead { font-size: 13.6px; line-height: 20.5px; color: var(--lead-grey); margin-bottom: 12px; }
  .column p { margin-bottom: 14px; }
  .session-label { color: var(--heading-blue); font-weight: 400; }

  .illustration {
    position: absolute; left: 850px; top: 500px; width: 350px; height: 351px;
    background: radial-gradient(ellipse at 45% 45%, #e9d6a6 0%, #c9a766 35%, rgba(255,255,255,0) 70%),
                radial-gradient(ellipse at 88% 88%, #9a4b22 0%, rgba(255,255,255,0) 40%);
  }
</style>
</head>
<body>
<main class="spread">
  <div class="edge-tab edge-tab--left"></div>
  <div class="edge-tab edge-tab--right"></div>

  <section class="column column--left">
    <h1 class="page-title">General Course Description</h1>
    <h2 class="section-title">Aim of the course</h2>
    <p class="lead">The goal of the course is to give learning-by-doing training in cross-examination for lawyers and experts from civil law countries, who may have limited opportunity to learn cross-examination in their domestic practice.</p>
    <p>The course is for 1.5 days and is divided into three sub-parts:</p>
    <p><span class="session-label">1st Session</span> (1st Day – Morning Session): The first session is dedicated to learning the basics of cross-examination, including how to prepare the expert for the cross.</p>
    <p><span class="session-label">2nd Session</span> (1st Day – Afternoon Session): The second session is dedicated to doing practical exercises of cross-examination.</p>
    <p><span class="session-label">3rd Session</span> (2nd Day – Morning Session): The third session is dedicated to repeating weak spots and also to learning new forms of expert examination, such as ‘hot tubbing’ or ‘witness conferencing’.</p>
    <p>Participants are limited to a maximum number of 32 and are divided into four groups: two are assigned the role of the Claimant and the other two the role of the Respondent. Each group has a maximum of 8 participants, among which 6-7 act as the party’s counsel and 1-2 participants act as the Experts appointed by such party. These assignments remain throughout the course. Each group is coached by a team of three instructors (i.e. 3 instructors for 8 participants).</p>
    <p>While there are some lectures and demonstrations, the vast majority of the course is dedicated to having the participants do cross-examination. Each participant acting as counsel will do at least one cross-examination and be a witness at least once (being a witness is also a valuable part of the learning experience, as is watching the other participants.). Each participant acting as Expert will be subject to at least two cross-examinations by the participants acting as counsel. Each cross-examination lasts from 10 to 14 minutes and each participant is videotaped.</p>
    <p>Two instructors give brief critiques after each Exercise. In addition, each participant will receive individual comments from a third instructor using the videotape of the participant’s performance (this is often the most effective part of the training).</p>
    <p>The faculty consists of experienced instructors from the US, most of whom have also taught abroad, but also instructors from Asia and Europe, who have extensive experience acting as counsel or arbitrators in international arbitration proceedings. This diversity in background and</p>
  </section>

  <section class="column column--right">
    <p>experience ensures that the participants are exposed to the different approaches that an arbitral tribunal may take to cross examination, depending on the background and nationality of the individual arbitrators.</p>
    <p>To make the exercise as realistic as possible, the course is based on a real case adapted to the needs of the exercise. The participants are given the case in advance (contracts, correspondence, demand for arbitration and response, witness statements, expert witness reports, etc.) for them to prepare.</p>
    <p>The course will be conducted in English but the experience gained from the course is readily portable into any language. Some of the instructors also speak Chinese and will be able to assist in case of language issues.</p>
    <p>While the atmosphere is informal with continuous interplay between instructors and participants, the course is quite intensive and yields very tangible results, which can immediately be put into practice.</p>
    <p>The course is based on the instructional method of the Institute for Advocacy Practice (IAP). IAP has 40 years of experience in both public programs teaching trial advocacy and deposition practice in the U.S., as well as private programs for law firms and government agencies in the United States and overseas. (For an overview of its activities, see the IAP website at www.iap-advocacy.org.)</p>
  </section>

  <div class="illustration" role="img" aria-label="Golden scales of justice with a wooden gavel in the corner"></div>
</main>
</body>
</html>
```